Power point for business plan needed for an adult entertainment app and website

Power point / catalogue/ business plan

Will be sent via pdf as a catalog and presented in tv screens via power point.
Should be very sexual and sexy.
The app colours are purple and dark pinks. Check logo below.
The information is in the pdf attached below.

Target Market(s)

Investors who like to invest in apps and online businesses.

Industry/Entity Type

dating app

Font styles to use
Serif
Decorative
Script

Colors
A7469A
B969AE
D3A5CF
EDDBEB
F8F0F9
6B429C
8869AF
B7A5CE
E3DAEB
F3F0F8

Requirements
Must have
• Sleek modern design with pictures that match the information.
Nice to have
• Capable of turning into a catalog or magazine style for display
Should not have
• Slides should not be word heavy.

```html
<!DOCTYPE html>
<html lang="en">
<head>
<meta charset="utf-8">
<title>App Feature List</title>
<link href="https://fonts.googleapis.com/css2?family=Playfair+Display:wght@500;600;700&family=Cormorant+Garamond:wght@400;500;600&family=Great+Vibes&display=swap" rel="stylesheet">
<style>
:root{
  --page:#ffffff;
  --slide:#1a0f22;
  --slide-deep:#120a19;
  --ink:#f8f0f9;
  --muted:#e3daeb;
  --soft:#d3a5cf;
  --ghost:#3a2248;
  --accent:#a7469a;
  --accent-light:#b969ae;
  --violet:#6b429c;
  --violet-light:#8869af;
  --lilac:#b7a5ce;
}
*{margin:0;padding:0;box-sizing:border-box}
html,body{width:900px;height:1200px;overflow:hidden;background:var(--page)}
body{position:relative;font-family:'Cormorant Garamond',serif;color:var(--ink)}
.slide{position:absolute;width:362px;height:207px;background:linear-gradient(135deg,var(--slide) 0%,var(--slide-deep) 100%);overflow:hidden;box-shadow:0 4px 14px rgba(40,10,50,.35)}
.col-left{left:57px}.col-right{left:470px}
.row-1{top:44px}.row-2{top:272px}.row-3{top:499px}.row-4{top:727px}.row-5{top:955px}
.abs{position:absolute}
.photo{position:absolute}
.heading{font-family:'Playfair Display',serif;font-weight:600;text-transform:uppercase;letter-spacing:.8px;line-height:1.15}
.body-copy{font-weight:500;font-size:5.6px;line-height:1.4;color:var(--muted);text-align:justify}
.body-copy p+p{margin-top:3px}
.rule{position:absolute;height:.7px;background:var(--accent)}
.bullets{list-style:none;font-weight:500;color:var(--muted)}
.bullets li{position:relative;padding-left:7px}
.bullets li::before{content:"";position:absolute;left:0;top:.55em;width:2px;height:2px;border-radius:50%;background:var(--accent-light)}
.script{font-family:'Great Vibes',cursive;font-weight:400}

/* cover */
.cover-bar{left:28px;top:36px;width:1.2px;height:82px;background:var(--accent)}
.cover-title{left:35px;top:34px;font-size:23px;font-weight:700;line-height:1.15}
.cover-sub{left:35px;top:132px;font-size:6.4px;letter-spacing:.6px;line-height:1.35;color:var(--soft)}
.cover-date{left:44px;top:190px;font-size:5.4px;color:var(--muted)}
/* intro */
.intro-title{left:27px;top:76px;font-size:13px}
.intro-copy{left:27px;top:100px;width:122px}
/* how */
.how-title{left:27px;top:32px;font-size:13px}
.how-copy{left:27px;top:100px;width:127px}
/* vendor */
.vendor-title{left:183px;top:20px;font-size:13px}
.vendor-list{left:183px;top:62px;width:158px;font-size:5.4px;line-height:1.35}
.vendor-list li{margin-bottom:2.6px}
/* customer */
.customer-title{left:27px;top:76px;font-size:13px}
.customer-list{left:170px;top:32px;width:128px;font-size:6.6px;line-height:1.3}
.customer-list li{margin-bottom:4px}
.ghost-word{color:var(--ghost);transform-origin:left top;transform:rotate(-90deg);white-space:nowrap}
/* master */
.master-title{left:0;width:100%;top:18px;text-align:center;font-size:13px}
.master-list{font-size:5.2px;line-height:1.35}
.master-list li{margin-bottom:4px}
/* web */
.web-title{left:27px;top:28px;font-size:13px}
.web-steps{left:32px;top:86px;width:112px;list-style:none}
.web-steps li{display:flex;gap:6px;margin-bottom:9px}
.web-steps .num{font-family:'Playfair Display',serif;font-size:11px;font-weight:600;line-height:1;color:var(--soft)}
.web-steps .txt{font-size:5.8px;font-weight:500;line-height:1.35;color:var(--muted)}
/* description */
.desc-title{left:0;width:100%;top:12px;text-align:center;font-size:13px}
.desc-col{top:60px;width:84px}
.desc-col h3{font-family:'Playfair Display',serif;font-size:6px;font-weight:600;color:var(--accent-light);margin-bottom:4px;letter-spacing:.5px}
.desc-col p{margin-bottom:3px}
/* why */
.why-title{left:206px;top:24px;font-size:13px;text-transform:none;font-weight:500}
.why-copy{left:206px;top:72px;width:133px}
/* thanks */
.thanks-kicker{left:178px;top:74px;font-size:12px;color:var(--soft)}
.thanks-title{left:176px;top:90px;font-size:26px;font-weight:700;line-height:1.1}
</style>
</head>
<body>

<section class="slide col-left row-1">
  <svg class="photo" width="362" height="207" viewBox="0 0 362 207" role="img" aria-label="Close-up figure photograph with a cherry">
    <defs><linearGradient id="g1" x1="0" y1="0" x2="1" y2="1"><stop offset="0" stop-color="#8869af"/><stop offset=".6" stop-color="#4a2a5e"/><stop offset="1" stop-color="#1a0f22"/></linearGradient></defs>
    <polygon points="252,0 362,0 362,60 255,207 140,207" fill="url(#g1)"/>
  </svg>
  <svg class="abs" style="left:0;top:0" width="362" height="207" viewBox="0 0 362 207">
    <g fill="none" stroke="#a7469a" stroke-width=".7">
      <polyline points="100,207 200,88 205,95 112,207"/>
      <line x1="126" y1="207" x2="206" y2="110"/>
      <line x1="362" y1="52" x2="250" y2="207"/>
      <line x1="362" y1="58" x2="256" y2="207"/>
    </g>
  </svg>
  <div class="abs cover-bar"></div>
  <h1 class="abs heading cover-title">APP<br>FEATURE<br>LIST</h1>
  <p class="abs cover-sub">Service provider, escort,<br>dating style app setup</p>
  <p class="abs cover-date">May, 25 2022</p>
</section>

<section class="slide col-right row-1">
  <svg class="photo" style="left:160px;top:26px" width="160" height="160" viewBox="0 0 160 160">
    <defs><radialGradient id="g2" cx=".55" cy=".45" r=".6"><stop offset="0" stop-color="#b7a5ce"/><stop offset=".5" stop-color="#6b429c"/><stop offset="1" stop-color="#1a0f22"/></radialGradient></defs>
    <circle cx="77" cy="78" r="73" fill="url(#g2)" role="img" aria-label="Figure study photograph in a circle"/>
    <path d="M 100 6 A 76 76 0 0 1 110 148" fill="none" stroke="#a7469a" stroke-width="6"/>
  </svg>
  <h2 class="abs heading intro-title">APP FEATURE LIST</h2>
  <div class="abs body-copy intro-copy">
    <p>Service provider, escort, dating style app setup.</p>
    <p>Users create accounts with an email address and password. Service providers get a unique link to share their listing on social media.</p>
  </div>
</section>

<section class="slide col-left row-2">
  <div class="photo" style="left:179px;top:0;width:183px;height:207px;background:radial-gradient(ellipse at 55% 55%,#b969ae 0%,#4a2a5e 45%,#120a19 80%)" role="img" aria-label="Photograph of a reclining figure with striped shadows"></div>
  <h2 class="abs heading how-title">HOW SERVICE<br>PROVIDER APP<br>WILL WORK</h2>
  <div class="rule" style="left:27px;top:92px;width:127px"></div>
  <div class="abs body-copy how-copy">
    <p>Our QuickDish like app is a user friendly on demand ordering app. Register or login, then search your favorite Vendor or use the filter option.</p>
    <p>Pay by debit/credit card or with your wallet money, and track your order to your door step by GPS.</p>
  </div>
</section>

<section class="slide col-right row-2">
  <svg class="photo" width="362" height="207" viewBox="0 0 362 207" role="img" aria-label="Side profile figure photograph">
    <defs><linearGradient id="g4" x1="0" y1="0" x2="1" y2="0"><stop offset="0" stop-color="#1a0f22"/><stop offset=".7" stop-color="#8869af"/><stop offset="1" stop-color="#2e1a3c"/></linearGradient></defs>
    <path d="M0,0 H140 C170,20 170,60 145,95 C125,125 160,160 125,207 H0 Z" fill="url(#g4)"/>
    <path d="M140,0 C172,20 172,60 147,95 C127,125 162,160 127,207" fill="none" stroke="#a7469a" stroke-width=".8"/>
  </svg>
  <h2 class="abs heading vendor-title">VENDOR ADMIN<br>PANEL MODULES:</h2>
  <ul class="abs bullets vendor-list">
    <li>Service provider registration</li>
    <li>Add / update details</li>
    <li>Online / offline modes for messaging</li>
    <li>Online available time slots for booking</li>
    <li>Upload pics and videos to profile</li>
    <li>Update list of services available</li>
    <li>Accept booking before it is confirmed</li>
    <li>All online payments held until provider and user mark completed</li>
    <li>Completed funds released to the provider's wallet, cash out by e-transfer</li>
  </ul>
</section>

<section class="slide col-left row-3">
  <div class="photo" style="left:40px;top:6px;width:90px;height:60px;background:radial-gradient(ellipse at 50% 70%,#b969ae 0%,#4a2a5e 55%,transparent 80%)" role="img" aria-label="Figure photograph, pose with raised arm"></div>
  <div class="photo" style="left:45px;top:130px;width:80px;height:77px;background:radial-gradient(ellipse at 50% 55%,#b969ae 0%,#4a2a5e 55%,transparent 80%)" role="img" aria-label="Figure photograph, arms raised overhead"></div>
  <h2 class="abs heading customer-title">CUSTOMER APP<br>MODULES:</h2>
  <div class="rule" style="left:27px;top:112px;width:36px"></div>
  <ul class="abs bullets customer-list">
    <li>Customer registration</li>
    <li>Update profile / settings, wants, likes. Create a profile</li>
    <li>Upload pics private until given access to service provider</li>
    <li>Wallet to book and pay online, load money with credit card or prepaid gift cards</li>
    <li>Review service providers, only 1 review per user, cannot edit or delete once posted</li>
  </ul>
  <div class="abs ghost-word script" style="left:316px;top:190px;font-size:44px">Modules</div>
</section>

<section class="slide col-right row-3">
  <div class="rule" style="left:17px;top:29px;width:78px"></div>
  <div class="rule" style="left:267px;top:29px;width:78px"></div>
  <h2 class="abs heading master-title">MASTER ADMIN PANEL:</h2>
  <ul class="abs bullets master-list" style="left:20px;top:46px;width:150px">
    <li>Approve listings</li>
    <li>Edit listing categories</li>
    <li>Manage main wallet of ad and premium payments</li>
    <li>Adjust listing prices</li>
    <li>Remove reviews</li>
    <li>Mark user as verified</li>
    <li>Mark user as diamond premium ***** 5 star service provider</li>
  </ul>
  <ul class="abs bullets master-list" style="left:184px;top:46px;width:158px">
    <li>Diamond premium is always highlighted and listed first</li>
    <li>Diamond premium listings bid on the top 3 spots of their area each week</li>
    <li>Bids end Sunday at 1pm; winners are locked in for the week</li>
    <li>Approve all bid winners</li>
    <li>Message vendors and users as admin</li>
  </ul>
  <div class="photo" style="left:4px;top:142px;width:340px;height:65px;background:linear-gradient(180deg,transparent 0%,#4a2a5e 45%,#8869af 62%,#1a0f22 100%)" role="img" aria-label="Panoramic photograph of a reclining figure split into panels"></div>
</section>

<section class="slide col-left row-4">
  <div class="photo" style="left:200px;top:50px;width:162px;height:110px;background:radial-gradient(ellipse at 50% 45%,#8869af 0%,#3a2248 50%,transparent 75%)" role="img" aria-label="Close-up figure photograph"></div>
  <svg class="abs" style="left:170px;top:52px" width="40" height="100" viewBox="0 0 40 100"><polyline points="28,2 4,50 28,98" fill="none" stroke="#a7469a" stroke-width="6"/></svg>
  <h2 class="abs heading web-title">WEB PAGE<br>(WEBAPP)</h2>
  <div class="rule" style="left:27px;top:72px;width:66px"></div>
  <ol class="abs web-steps">
    <li><span class="num">01</span><span class="txt">Same info as the OrbitOS and NovaOS APP, Admin Panel and MASTER control.</span></li>
    <li><span class="num">02</span><span class="txt">ALL the same functions, synced across every platform.</span></li>
    <li><span class="num">03</span><span class="txt">Vendor may set their Hours on calendar and availability.</span></li>
  </ol>
</section>

<section class="slide col-right row-4">
  <div class="photo" style="left:0;top:82px;width:362px;height:125px;background:linear-gradient(180deg,transparent 0%,#3a2248 30%,#6b429c 55%,#2e1a3c 80%,#1a0f22 100%)" role="img" aria-label="Photograph of soft body contours"></div>
  <div class="rule" style="left:36px;top:30px;width:93px"></div>
  <div class="rule" style="left:233px;top:30px;width:93px"></div>
  <h2 class="abs heading desc-title">DESCRIPTION<br>AND DETAILS</h2>
  <div class="abs body-copy desc-col" style="left:37px">
    <h3>ESCORTS</h3>
    <p>The safest most reliable way to book your well-deserved time. Funds are held until you confirm completed.</p>
    <p>No cash on hand keeps the provider safe too.</p>
  </div>
  <div class="abs body-copy desc-col" style="left:139px">
    <h3>GFE</h3>
    <p>Booked like our escort services, but paid by the meeting, whether it's a dinner and evening or a full weekend.</p>
    <p>Have a true Girl Friend Experience (GFE).</p>
  </div>
  <div class="abs body-copy desc-col" style="left:241px">
    <h3>MASSAGE</h3>
    <p>Our massage providers offer different services, message them before you book.</p>
    <h3 style="margin-top:4px">FETISH</h3>
    <p>List your fetish in your profile. No one's here to judge you. The sky is the limit here, just message and ask.</p>
  </div>
</section>

<section class="slide col-left row-5">
  <div class="photo" style="left:0;top:30px;width:150px;height:177px;background:radial-gradient(ellipse at 60% 55%,#d3a5cf 0%,#6b429c 35%,#1a0f22 70%)" role="img" aria-label="Macro photograph of skin with water droplets"></div>
  <div class="abs ghost-word script" style="left:128px;top:150px;font-size:44px;color:#5a3470">Why</div>
  <h2 class="abs heading why-title">Why List Your Ad<br>With Us?</h2>
  <div class="rule" style="left:206px;top:64px;width:100px"></div>
  <div class="abs body-copy why-copy">
    <p>We are the premium service provider site, keeping you independent and safe, with secure rooms and security personnel in select cities.</p>
    <p>Clients pre pay to book online, no more no shows, no more getting scammed. Add a gift wish list to your profile and users can donate towards it.</p>
  </div>
</section>

<section class="slide col-right row-5">
  <div class="photo" style="left:22px;top:62px;width:130px;height:88px;background:radial-gradient(ellipse at 50% 45%,#b7a5ce 0%,#6b429c 45%,#1a0f22 80%)" role="img" aria-label="Photograph of ice cubes on wet skin"></div>
  <p class="abs thanks-kicker script">See you agin next time !</p>
  <h2 class="abs heading thanks-title">THANK YOU</h2>
  <div class="rule" style="left:178px;top:124px;width:110px"></div>
</section>

</body>
</html>
```